Modern, clean and professional Wordpress design for a safety training company!

We are currently in the process of creating a new website for our business. We have hired a website developer and the main structure of our new Wordpress site is complete. We now need an overall design plan for the site. We need a very clean, professional and easy to follow website. Most of our website visitors only spend about 30-45 secs on our sites "shopping " so it is imperative that we have a strong Home Page.
Our company specializes in CPR and First Aid Certification Classes to businesses and individuals throughout Northern California. We provide these certifications two ways: ONSITE-We come to you, and HOSTED-we offer weekly classes at our 2 locations.
Our design needs to use the general green and blue colors of our logo. But we also like white.
The final design MUST communicate a legitimate, trustworthy and professional business. Our industry is VERY competitive and we need to STAND OUT.
Currently, the NEW website that we need a new design for is www.LifelineSkillsHub.com
Our old website is www.RescueCoursesValley.com and we really do like the design of this website, but we just needed a Wordpress site for SEO purposes.
These are 3 websites that we really:
http://vorlandmedix.com/
http://www.pelbrik.com/
https://www.quimby.com/
I have attached our Logo and other images if you need to use them but looking at the current two sites will be you best help.
1) Large businesses and industries that are looking for a company to provide ONSITE safety training classes at their office or place of work.
2) Individuals that need certifications for their jobs and other needs. These individuals are looking for a legitimate, trustworthy and professional environment to complete their training class.

```html
<!DOCTYPE html>
<html lang="en">
<head>
<meta charset="utf-8">
<title>Crestline Safety Academy</title>
<link href="https://fonts.googleapis.com/css2?family=Open+Sans:wght@400;600;700&display=swap" rel="stylesheet">
<style>
:root{
  --navy:#0f2a78;
  --green:#6e8b12;
  --green-light:#8aa51f;
  --text:#8a8a8a;
  --dark-text:#2b2b2b;
  --band:#efefef;
  --footer:#1f1e2b;
  --white:#ffffff;
  --star:#f2952b;
}
*{margin:0;padding:0;box-sizing:border-box}
html,body{width:1200px;height:2293px;overflow:hidden;background:var(--white)}
body{font-family:"Open Sans",Arial,sans-serif;color:var(--text);position:relative}
.abs{position:absolute}

/* header */
.site-header{position:absolute;left:0;top:0;width:1200px;height:125px;background:var(--white);box-shadow:0 2px 6px rgba(0,0,0,.25);z-index:2}
.brand{position:absolute;left:99px;top:34px;display:flex;align-items:center;gap:12px}
.brand-mark{width:34px;height:34px;border-radius:50%;background:var(--green-light)}
.brand-name{font-size:19px;font-weight:700;color:var(--navy);line-height:1.15;width:130px}
.main-nav{position:absolute;top:55px;left:446px;display:flex;gap:0;font-size:12.5px;font-weight:600;color:#333;text-transform:uppercase}
.main-nav span{position:absolute;white-space:nowrap}
.main-nav .active::after{content:"";position:absolute;left:0;right:0;top:24px;height:4px;background:var(--navy)}

/* hero */
.hero{position:absolute;left:0;top:125px;width:1200px;height:612px;background:linear-gradient(160deg,#c9cdd0 0%,#9aa0a3 40%,#5b5e60 75%,#3b3c3e 100%)}
.hero-title{position:absolute;left:99px;top:458px;font-size:43px;font-weight:700;color:var(--white);letter-spacing:.5px}
.hero-sub{position:absolute;left:99px;top:527px;font-size:22px;font-weight:600;color:var(--white)}
.hero-dots{position:absolute;left:561px;top:703px;display:flex;gap:8px}
.hero-dots i{width:15px;height:15px;border:3px solid var(--white);border-radius:50%;background:rgba(0,0,0,.25)}
.hero-shadow{position:absolute;left:0;top:737px;width:1200px;height:20px;background:radial-gradient(ellipse at top,rgba(0,0,0,.22),rgba(0,0,0,0) 70%)}

/* welcome */
.section-title{position:absolute;left:0;width:1200px;text-align:center;font-size:17px;font-weight:700;color:var(--navy);text-transform:uppercase}
.welcome-intro{position:absolute;left:340px;top:808px;width:520px;text-align:center;font-size:12.5px;line-height:20px}
.welcome-photo{position:absolute;left:99px;top:877px;width:453px;height:254px;border:6px solid var(--white);box-shadow:0 0 3px rgba(0,0,0,.35);background:linear-gradient(135deg,#6b7f8a,#5a5d88 55%,#3a3f5c)}
.photo-shadow{position:absolute;left:110px;top:1131px;width:431px;height:16px;background:radial-gradient(ellipse at top,rgba(0,0,0,.25),rgba(0,0,0,0) 70%)}
.welcome-copy{position:absolute;left:591px;top:891px;width:510px}
.welcome-copy h3{font-size:12px;font-weight:700;color:var(--dark-text);line-height:21px;text-transform:uppercase}
.welcome-copy p{font-size:12.5px;line-height:20px;margin-top:15px}
.btn{display:inline-block;background:var(--green);color:var(--white);font-weight:700;font-size:14px;text-transform:uppercase;text-align:center;border-radius:2px}
.welcome-btn{position:absolute;left:592px;top:1078px;width:127px;height:43px;line-height:43px}

/* company band */
.company{position:absolute;left:0;top:1176px;width:1200px;height:486px;background:var(--band);border-bottom:1px solid #ddd}
.company-notes{position:absolute;left:0;top:1242px;width:1200px;text-align:center;font-size:12.5px;line-height:23px}
.course-card{position:absolute;top:1313px;width:317px;height:310px;background:var(--white);border:1px solid #ddd}
.course-photo{height:259px}
.course-caption{display:flex;justify-content:space-between;align-items:center;height:51px;padding:0 8px}
.course-name{font-size:17px;font-weight:700;color:var(--navy)}
.course-price{font-size:12px;font-style:italic;color:var(--green-light)}
.hover-cover{position:absolute;left:0;top:0;width:100%;height:259px;background:rgba(40,40,40,.65)}
.outline-btn{position:absolute;left:86px;top:108px;width:145px;height:44px;line-height:42px;border:1px solid var(--white);color:var(--white);font-size:13px;font-weight:700;text-align:center}

/* reviews */
.review{position:absolute;top:1738px;width:298px;height:145px;background:#ececec;text-align:center;font-size:11.5px;color:#333;padding-top:20px;line-height:21px}
.stars{color:var(--star);font-size:15px;letter-spacing:1px}

/* footer */
.site-footer{position:absolute;left:0;top:1926px;width:1200px;height:367px;background:var(--footer);color:#cfcfd6}
.footer-head{position:absolute;font-size:19px;color:var(--white)}
.field{position:absolute;width:205px;height:32px;background:var(--white);border-radius:2px;font-size:11px;color:#888;padding:9px 16px}
.check{position:absolute;left:324px;top:2129px;width:11px;height:11px;border:1px solid #444;background:#2a2a36}
.check-label{position:absolute;left:345px;top:2126px;font-size:11px;color:#6c6c78}
.submit{position:absolute;left:318px;top:2171px;width:205px;height:34px;line-height:34px;font-weight:400;text-transform:none;font-size:13px}
.footer-text{position:absolute;left:590px;top:2014px;width:386px;font-size:11px;line-height:20px;color:#6f6f7c}
.social{position:absolute;left:591px;top:2140px;display:flex;align-items:center;gap:10px;font-size:14px;color:var(--white)}
.social i{width:28px;height:28px;border-radius:50%;background:#6a6a72;display:inline-block}
.footer-links{position:absolute;left:1020px;top:2014px;font-size:11px;line-height:25px;color:#8c8c98;list-style:none}
.copyright{position:absolute;left:0;top:2255px;width:1200px;text-align:center;font-size:11px;color:#6b6b78}
</style>
</head>
<body>

<header class="site-header">
  <div class="brand"><span class="brand-mark"></span><span class="brand-name">CSA Crestline Safety</span></div>
  <nav class="main-nav">
    <span class="active" style="left:0">Home</span>
    <span style="left:65px">Class Calender</span>
    <span style="left:193px">Classes for Groups</span>
    <span style="left:347px">Certification Classes</span>
    <span style="left:514px">About Us</span>
    <span style="left:601px">Policies</span>
  </nav>
</header>

<section class="hero" role="img" aria-label="Photo of a classroom with students listening to an instructor"></section>
<h1 class="hero-title">CPR+FIRST AID $59</h1>
<p class="hero-sub">ADULT/CHILD/INFANT 3 HOURS OR LESS!</p>
<div class="hero-dots"><i></i><i></i><i></i><i></i></div>
<div class="hero-shadow"></div>

<h2 class="section-title" style="top:774px">Welcome to Crestline Safety Academy!</h2>
<p class="welcome-intro">Crestline Safety Academy is Northern California's leader in CPR, BLS, and Basic First Aid Certifications!</p>
<div class="welcome-photo" role="img" aria-label="Photo of medical staff in scrubs practicing emergency care"></div>
<div class="photo-shadow"></div>
<div class="welcome-copy">
  <h3>Taught by experienced firefighters, our classes are much shorter and provide common sense knowledge and skills to each student to</h3>
  <p>By using real life emergency responders, we have revolutionized the standard, boring CPR class by teaching students the need-to-know information and preparing them with facts and tips to help them in true life and death situations!</p>
  <p>Crestline Safety Academy is Northern California's leader in CPR, BLS, and Basic First Aid Certifications! Taught by experienced Firefighters,&nbsp; them for actual emergencies.</p>
</div>
<a class="btn welcome-btn">Read More</a>

<section class="company"></section>
<h2 class="section-title" style="top:1209px;color:#333">Company</h2>
<p class="company-notes">1. Registering/Paying Online will GUARANTEE your seat in class AND you will receive your certification the day of class!<br>2 . Registering ONLY will NOT guarantee your seat in class and your certification will be mailed to you within 1-2 business days.</p>

<article class="course-card" style="left:98px">
  <div class="course-photo" role="img" aria-label="Photo of a nurse practicing CPR compressions" style="background:linear-gradient(135deg,#4a5a70,#8a8fa6 50%,#3d3f55)"></div>
  <div class="course-caption"><span class="course-name">CPR</span><span class="course-price">$39 Adult/Child/Infant 90 Minutes!</span></div>
</article>
<article class="course-card" style="left:440px">
  <div class="course-photo" role="img" aria-label="Photo of a classroom audience during a course" style="background:linear-gradient(135deg,#9a9da0,#6c6f72)"></div>
  <div class="hover-cover"><span class="outline-btn">READ MORE</span></div>
  <div class="course-caption"><span class="course-name" style="padding-left:8px">BLS</span><span class="course-price">$49 Healthcare/Dental 90 Minutes!</span></div>
</article>
<article class="course-card" style="left:784px">
  <div class="course-photo" role="img" aria-label="Photo of CPR training mannequins on a table in a classroom" style="background:linear-gradient(160deg,#b9bcc0,#e2e2e4 55%,#8e9096)"></div>
  <div class="course-caption"><span class="course-name" style="padding-left:5px">CPR+FIRST AID</span><span class="course-price">$59&nbsp; Adult/Child/Infant</span></div>
</article>

<h2 class="section-title" style="top:1694px">Reviews</h2>
<div class="review" style="left:99px"><div class="stars">★★★★☆</div>Marissa- CA, United States<br>February 3, 2014<br>The instructor was great--he was a...</div>
<div class="review" style="left:451px"><div class="stars">★★★★☆</div>Marissa- CA, United States<br>February 3, 2014<br>The instructor was great--he was a...</div>
<div class="review" style="left:804px"><div class="stars">★★★★☆</div>Marissa- CA, United States<br>February 3, 2014<br>The instructor was great--he was a...</div>

<footer class="site-footer"></footer>
<h3 class="footer-head" style="left:99px;top:1972px">Subscribe to newsletter</h3>
<div class="field" style="left:99px;top:2026px">Business Name</div>
<div class="field" style="left:318px;top:2026px">Contact Name</div>
<div class="field" style="left:99px;top:2072px">Email Address</div>
<div class="field" style="left:318px;top:2072px">Type of Business</div>
<div class="field" style="left:99px;top:2119px">Website Address</div>
<span class="check"></span><span class="check-label">Subscribe to newsletter</span>
<a class="btn submit">Submit Now</a>

<h3 class="footer-head" style="left:590px;top:1972px">At vero eos et accusamus</h3>
<p class="footer-text">At vero eos et accusamus et iusto odio dignissimos ducimus qui blanditiis praesentium voluptatum deleniti atque corrupti quos dolores et quas molestias excepturi sint occaecati cupiditate non provident,&nbsp; Nam libero tempore, cum soluta nobis est eligendi optio cumque nihil impedit quo minus id quod maxime placeat facere possimus.</p>
<div class="social">Connect with our social network :&nbsp; <i></i><i></i><i></i></div>

<h3 class="footer-head" style="left:1018px;top:1972px">Welcome</h3>
<ul class="footer-links"><li>Home</li><li>About us</li><li>How it works</li><li>Pricing</li><li>Contact Us</li></ul>

<p class="copyright">Copyright © 2014 Crestline. All rights reserved.</p>

</body>
</html>
```